New Company Business Card Design

I have a new company logo and I want a new business card design. I dont know if the logo file i attached is in the correct format or quality. We are a New York City Specialty construction Firm specializing in high risk out of the box projects. I want a simple and classy business card that people will his card is as crisp as the work his company does.

Target Market(s)

Clients in the heavy construction industry in New York City

Industry/Entity Type

Construction Company

Contact Information for Business Card

Simple Classy - DIFFERENT

Font styles to use
Other font styles liked:
• Mach the logo font in some way

Colors

Designer to choose colors to be used in the design.

Requirements
Must have
• Uniqueness
Nice to have
• Nothing particular - Just different and classy - Timeless
Should not have
• Goofy Shit or Gimmicky shit

```html
<!DOCTYPE html>
<html lang="en">
<head>
<meta charset="utf-8">
<title>Halvern Associates – Business Cards</title>
<link href="https://fonts.googleapis.com/css2?family=Lato:wght@400;700;900&display=swap" rel="stylesheet">
<style>
  :root {
    --backdrop: #dcdde1;
    --paper: #ebecee;
    --charcoal: #3f3f3f;
    --panel-top: #414141;
    --panel-bottom: #252525;
    --brand-blue: #1b8ad0;
    --ink: #454545;
    --name-grey: #c9c9c9;
    --detail-grey: #d2d2d2;
  }
  * { margin: 0; padding: 0; box-sizing: border-box; }
  html, body {
    width: 1200px; height: 1200px; overflow: hidden;
    background: var(--backdrop);
    font-family: 'Lato', sans-serif;
  }
  .card {
    position: absolute; left: 285px; width: 630px; height: 360px;
    background: var(--paper); overflow: hidden;
  }
  .card--front { top: 194px; }
  .card--back { top: 646px; }

  .front-edge {
    position: absolute; left: 0; top: 0; width: 26px; height: 100%;
    background: var(--charcoal);
  }
  .brand {
    position: absolute; display: flex; align-items: center; gap: 10px;
    transform: translate(-50%, -50%);
    color: var(--brand-blue); font-weight: 900; white-space: nowrap;
    line-height: 1.05; text-transform: uppercase; text-align: center;
  }
  .brand__mark { background: var(--brand-blue); flex: none; }
  .card--front .brand { left: 328px; top: 180px; font-size: 30px; letter-spacing: 1px; }
  .card--front .brand__mark { width: 26px; height: 26px; }
  .card--back .brand { left: 151px; top: 186px; font-size: 22px; letter-spacing: 0.5px; }
  .card--back .brand__mark { width: 19px; height: 19px; }
  .brand__name { display: block; }

  .front-contact {
    position: absolute; left: 26px; right: 0; top: 303px;
    text-align: center; font-size: 16.5px; font-weight: 700;
    color: var(--ink); letter-spacing: 0.2px;
  }

  .back-panel {
    position: absolute; left: 302px; top: 0; width: 328px; height: 360px;
    background: linear-gradient(160deg, var(--panel-top) 0%, var(--panel-bottom) 100%);
  }
  .contact-rail { position: absolute; left: 0; top: 0; }
  .holder-name {
    position: absolute; left: 92px; top: 82px;
    font-size: 19.5px; font-weight: 700; color: var(--name-grey);
    letter-spacing: 0.1px;
  }
  .holder-address {
    position: absolute; left: 95px; top: 136px;
    font-size: 13px; font-weight: 700; color: var(--detail-grey); line-height: 15.5px;
  }
  .holder-lines {
    position: absolute; left: 94px; top: 200px; list-style: none;
    font-size: 14px; font-weight: 700; color: var(--detail-grey); line-height: 24px;
  }
</style>
</head>
<body>

<section class="card card--front">
  <div class="front-edge"></div>
  <div class="brand">
    <span class="brand__mark"></span>
    <span class="brand__name">Halvern<br>Associates, Inc.</span>
  </div>
  <p class="front-contact">PHONE: 908-555-0142 &nbsp;|&nbsp; WEBSITE: HALVERN.COM</p>
</section>

<section class="card card--back">
  <div class="brand">
    <span class="brand__mark"></span>
    <span class="brand__name">Halvern<br>Associates, Inc.</span>
  </div>

  <div class="back-panel">
    <svg class="contact-rail" width="328" height="360" viewBox="0 0 328 360" aria-hidden="true">
      <g stroke="var(--brand-blue)" stroke-width="2">
        <line x1="59" y1="113" x2="59" y2="132"/>
        <line x1="59" y1="170" x2="59" y2="186"/>
      </g>
      <polygon points="59,75 76,85 76,104 59,114 42,104 42,85" fill="var(--brand-blue)"/>
      <polygon points="59,132 75,141.5 75,160.5 59,170 43,160.5 43,141.5" fill="none" stroke="var(--brand-blue)" stroke-width="2.5"/>
      <polygon points="59,186 76,198 76,270 59,282 42,270 42,198" fill="var(--brand-blue)"/>
      <!-- person -->
      <g fill="#fff">
        <circle cx="59" cy="90" r="4"/>
        <path d="M51.5 101 q0-7 7.5-7 q7.5 0 7.5 7 z"/>
      </g>
      <!-- pin -->
      <path d="M59 159 c-4-5-6-8-6-11 a6 6 0 0 1 12 0 c0 3-2 6-6 11z" fill="#fff"/>
      <circle cx="59" cy="148" r="2.2" fill="var(--brand-blue)"/>
      <!-- phone -->
      <g fill="#fff">
        <path d="M51 208 q8-5 16 0 v2 h-3 v-1.5 q-5-2-10 0 v1.5 h-3z"/>
        <rect x="53" y="210" width="12" height="5" rx="1"/>
      </g>
      <!-- mail -->
      <g>
        <rect x="51.5" y="229" width="15" height="10" fill="#fff"/>
        <polyline points="51.5,229 59,235 66.5,229" fill="none" stroke="var(--brand-blue)" stroke-width="1.2"/>
      </g>
      <!-- globe -->
      <g fill="none" stroke="#fff" stroke-width="1.1">
        <circle cx="59" cy="258" r="7"/>
        <ellipse cx="59" cy="258" rx="3" ry="7"/>
        <line x1="52" y1="258" x2="66" y2="258"/>
        <line x1="53.5" y1="254" x2="64.5" y2="254"/>
        <line x1="53.5" y1="262" x2="64.5" y2="262"/>
      </g>
    </svg>

    <h2 class="holder-name">MARCUS T. RINALDI</h2>
    <p class="holder-address">415 Harbor Point Road - Linden,<br>New Jersey 07036</p>
    <ul class="holder-lines">
      <li>917-555-0187</li>
      <li>mrinaldi@halvern.com</li>
      <li>www.halvern.com</li>
    </ul>
  </div>
</section>

</body>
</html>
```